Velvet & Bloom Hair Extensions needs a business card

We need a business card designed for an online luxury hair extensions business called Velvet & Bloom, we already have a logo and need an innovative business card (2-sided preferably). The strap line for the brand is 'Luxury Hair At Every Touchpoint!'. The brand is a premium brand selling virgin hair extensions and the target market is the mid-affluent ethnic woman as such the design should reflect this. The brand logo is grey and can be sent when requested.

Target Market(s)

25 to 35 year mid-affluent ethnic woman (Afro-American, Mixed Race, Asian)

Industry/Entity Type

Hair

Colors

Designer to choose colors to be used in the design.

Requirements
Must have
• Business Name: Velvet and Bloom
Strapline: Luxury hair at every touchpoint!
Domain: ​www.velvetandbloom-demo.com
Email: info@velvetandbloom-demo.com
sales and enquiries
44 07391 xxxxxxx

Please use the grey main brand logo depicted in page 2 of the attached pdf document

```html
<!DOCTYPE html>
<html lang="en">
<head>
<meta charset="utf-8">
<title>Velvet &amp; Bloom Hair Extensions – Business Card</title>
<link rel="stylesheet" href="https://fonts.googleapis.com/css2?family=Arimo:wght@400;700&family=Tangerine:wght@700&display=swap">
<style>
  :root {
    --backdrop: #1f2a3d;
    --peach-light: #efcfa8;
    --peach-mid: #dea070;
    --copper: #c9784a;
    --copper-deep: #a9552b;
    --teal: #13aa9a;
    --ink: #1a1412;
    --script-ink: #2b1a12;
    --icon-brown: #6b3418;
    --band: #1c1b1c;
    --hair-light: #b07a4a;
    --hair-dark: #5a3520;
  }
  * { margin: 0; padding: 0; box-sizing: border-box; }
  html, body {
    width: 1200px; height: 970px; overflow: hidden;
    background: var(--backdrop);
  }
  .stage { position: relative; width: 1200px; height: 970px; }

  .card {
    position: absolute;
    overflow: hidden;
    background:
      radial-gradient(ellipse 60% 80% at 18% 55%, var(--peach-light) 0%, rgba(239,207,168,0) 70%),
      radial-gradient(ellipse 55% 70% at 95% 95%, var(--copper-deep) 0%, rgba(169,85,43,0) 70%),
      linear-gradient(100deg, var(--peach-mid) 0%, var(--copper) 100%);
  }
  .card--front { left: 66px; top: 32px; width: 712px; height: 426px; }
  .card--back  { left: 321px; top: 481px; width: 777px; height: 466px; }

  .brand {
    position: absolute;
    display: flex; align-items: center;
    font-family: "Arimo", Arial, sans-serif;
    font-weight: 700;
    color: var(--teal);
    white-space: nowrap;
  }
  .brand__mark { background: var(--teal); flex: none; }

  .card--front .brand { left: 210px; top: 280px; font-size: 36px; gap: 14px; }
  .card--front .brand__mark { width: 40px; height: 40px; }

  .card--back .brand { left: 34px; top: 160px; font-size: 23px; gap: 9px; }
  .card--back .brand__mark { width: 26px; height: 26px; }

  .strapline {
    position: absolute;
    font-family: "Tangerine", cursive;
    font-weight: 700;
    color: var(--script-ink);
    white-space: nowrap;
  }
  .card--front .strapline { left: 192px; top: 352px; font-size: 38px; }
  .card--back .strapline { left: 27px; top: 206px; font-size: 23px; }

  .contact {
    position: absolute; left: 60px; top: 262px;
    list-style: none;
    font-family: "Arimo", Arial, sans-serif;
    font-size: 19px; color: var(--ink);
  }
  .contact__item { display: flex; align-items: center; height: 33px; }
  .contact__icon { width: 22px; height: 22px; margin-right: 12px; flex: none; }
  .contact__item--plain { padding-left: 34px; }

  .portrait {
    position: absolute; right: 0; top: 0;
    width: 298px; height: 406px;
    background:
      radial-gradient(ellipse 40% 35% at 50% 45%, #e2b394 0%, rgba(226,179,148,0) 100%),
      linear-gradient(160deg, var(--hair-light) 0%, var(--hair-dark) 100%);
  }

  .card__band {
    position: absolute; left: 0; bottom: 0;
    width: 100%; height: 60px; background: var(--band);
  }
</style>
</head>
<body>
<main class="stage">

  <section class="card card--front" aria-label="Business card front">
    <div class="brand"><span class="brand__mark"></span>Velvet &amp; Bloom</div>
    <p class="strapline">Luxury hair at every touchpoint!</p>
  </section>

  <section class="card card--back" aria-label="Business card back">
    <div class="brand"><span class="brand__mark"></span>Velvet &amp; Bloom</div>
    <p class="strapline">Luxury hair at every touchpoint!</p>

    <ul class="contact">
      <li class="contact__item">
        <svg class="contact__icon" viewBox="0 0 24 24" fill="none" stroke="var(--icon-brown)" stroke-width="1.8">
          <circle cx="12" cy="12" r="10"/><ellipse cx="12" cy="12" rx="4.5" ry="10"/>
          <line x1="2" y1="12" x2="22" y2="12"/><path d="M4 7h16M4 17h16"/>
        </svg>
        www.velvetandbloom-demo.com
      </li>
      <li class="contact__item">
        <svg class="contact__icon" viewBox="0 0 24 24">
          <rect x="2" y="5" width="20" height="14" fill="var(--icon-brown)"/>
          <path d="M2 5l10 8 10-8" fill="none" stroke="var(--peach-light)" stroke-width="1.5"/>
        </svg>
        info@velvetandbloom-demo.com
      </li>
      <li class="contact__item contact__item--plain">Sales &amp; Enquiry</li>
      <li class="contact__item">
        <svg class="contact__icon" viewBox="0 0 24 24">
          <circle cx="12" cy="12" r="10.5" fill="none" stroke="var(--icon-brown)" stroke-width="1.6"/>
          <path d="M8 6.5l2.2-.5 1.2 3-1.5 1.2c.7 1.6 1.8 2.7 3.4 3.4l1.2-1.5 3 1.2-.5 2.2c-4.5.4-9.4-4.5-9-9z" fill="var(--icon-brown)"/>
        </svg>
        44 07391 xxxxxxx
      </li>
    </ul>

    <div class="portrait" role="img" aria-label="Photograph of a woman with long, voluminous wavy brown hair"></div>
    <div class="card__band"></div>
  </section>

</main>
</body>
</html>
```